Entertainment Sound and Lighting company Business card

We need a professional looking business card designed for my growing entertainment sound and lighting company based in Sydney, Australia called "Kestrel Sound"

We provide technical production services (sound systems/lighting/vision) for events ranging from band gigs, weddings, corporate functions etc.

The business card needs to contain the following information:

Bartholomew Quenneville
Audio Engineer
Phone: 0478 615 702
Email: bartholomew@kestrelsound.com.au
Website: www.kestrelsound.com.au

Business logo has been attached in .ai format, please contact me if you need me to provide other files.

Target Market(s)

We need a business card that reflects our modern and professional company but still looks professional to appeal to our corporate clients.
We have a very broad target market spanning from bands needing PA systems for their gigs (18-30yrs) to event companies needing sound and lighting for weddings and other functions.

Industry/Entity Type

Business

Requirements
Must have
• Needs to include the logo that is attached of course, and the colour scheme.
Nice to have
• - Double sided

```html
<!DOCTYPE html>
<html lang="en">
<head>
<meta charset="utf-8">
<title>Kestrel Sound – Business Card</title>
<link rel="stylesheet" href="https://fonts.googleapis.com/css2?family=EB+Garamond:ital,wght@0,600;1,400&display=swap">
<style>
  :root {
    --brand-blue: #0aa3d9;
    --brand-navy: #1d6fb0;
    --card-white: #ffffff;
    --stage: #eceae6;
    --rule-blue: #7fd0ee;
    --card-w: 840px;
    --card-h: 480px;
  }
  * { box-sizing: border-box; margin: 0; padding: 0; }
  html, body {
    width: 964px;
    height: 1200px;
    overflow: hidden;
    background: var(--stage);
  }
  .sheet {
    width: 964px;
    height: 1200px;
    display: flex;
    flex-direction: column;
    align-items: center;
    justify-content: center;
    gap: 80px;
  }
  .card {
    position: relative;
    width: var(--card-w);
    height: var(--card-h);
    border-radius: 14px;
    overflow: hidden;
    box-shadow: 0 4px 14px rgba(0,0,0,0.12);
    display: flex;
    flex-direction: column;
    align-items: center;
    justify-content: center;
    text-align: center;
    font-family: "EB Garamond", Georgia, serif;
  }
  .card-edges {
    position: absolute;
    inset: 0;
    width: 100%;
    height: 100%;
  }
  .card-content {
    position: relative;
    display: flex;
    flex-direction: column;
    align-items: center;
  }
  .wordmark {
    display: flex;
    align-items: center;
    gap: 16px;
    font-family: "EB Garamond", Georgia, serif;
    font-weight: 600;
    font-style: normal;
    font-size: 64px;
    line-height: 1;
    letter-spacing: 0.5px;
  }
  .wordmark-dot {
    width: 26px;
    height: 26px;
    border-radius: 50%;
  }
  .divider {
    width: 430px;
    height: 2px;
    margin: 26px 0 18px;
  }
  .holder-name {
    font-style: italic;
    font-weight: 400;
    font-size: 26px;
  }

  /* Front */
  .card--front { background: var(--card-white); }
  .card--front .edge { fill: var(--brand-blue); }
  .card--front .wordmark { color: var(--brand-navy); }
  .card--front .wordmark-dot { background: var(--brand-blue); }
  .card--front .divider { background: linear-gradient(90deg, transparent, var(--rule-blue), transparent); }
  .card--front .holder-name { color: var(--brand-blue); }

  /* Back */
  .card--back { background: var(--brand-blue); color: var(--card-white); }
  .card--back .edge { fill: var(--card-white); }
  .card--back .wordmark { color: var(--card-white); font-size: 52px; }
  .card--back .wordmark-dot { background: var(--card-white); width: 22px; height: 22px; }
  .card--back .divider {
    margin: 22px 0 16px;
    background: linear-gradient(90deg, transparent, rgba(255,255,255,0.85), transparent);
  }
  .contact-list {
    list-style: none;
    font-style: italic;
    font-size: 21px;
    line-height: 1.4;
  }
  .contact-list .holder-name { font-size: 23px; }
</style>
</head>
<body>
<main class="sheet">

  <section class="card card--front" aria-label="Business card front">
    <svg class="card-edges" viewBox="0 0 840 480" preserveAspectRatio="none" aria-hidden="true">
      <path class="edge" d="M0 0 H840 V34 C620 8 220 8 0 20 Z"/>
      <path class="edge" d="M0 480 V462 C240 446 600 440 840 424 V480 Z"/>
    </svg>
    <div class="card-content">
      <div class="wordmark"><span class="wordmark-dot"></span>Kestrel Sound</div>
      <div class="divider"></div>
      <p class="holder-name">Bartholomew Quenneville</p>
    </div>
  </section>

  <section class="card card--back" aria-label="Business card back">
    <svg class="card-edges" viewBox="0 0 840 480" preserveAspectRatio="none" aria-hidden="true">
      <path class="edge" d="M0 0 H520 C360 10 180 18 0 40 Z"/>
      <path class="edge" d="M840 480 H300 C480 466 660 456 840 436 Z"/>
    </svg>
    <div class="card-content">
      <div class="wordmark"><span class="wordmark-dot"></span>Kestrel Sound</div>
      <div class="divider"></div>
      <ul class="contact-list">
        <li class="holder-name">Bartholomew Quenneville</li>
        <li class="contact-role">Audio Engineer</li>
        <li class="contact-phone">Phone: 0478 615 702</li>
        <li class="contact-email">Email: bartholomew@kestrelsound.com.au</li>
        <li class="contact-web">Website: www.kestrelsound.com.au</li>
      </ul>
    </div>
  </section>

</main>
</body>
</html>
```